Sole Relationship Graphic of Chapter Organization for Book

This design shows relationships between variables associated with footwear and footprints. It will be used as a graphic in a book. The four elements of the graphic are (1) Variables, (2) Book Chapter Numbers (which correspond to the relationship(s) between at least two variables, (3) Relationship Arrows, and (4) Influence Arrows (because the influencers affect the variables differently than relationships between the variables). These names simply relate to the attempts I have made (and attached) at creating a graphic. In the attached diagrams, the circles with numbers are placeholders for the book chapter numbers, which may be changed so it will be good if I can change those after the graphic is completed. Chapter 1 will be the introduction.
The intent of of outsourcing this project is not necessarily sticking to the formats I have attached, but to allow your creativity to produce a useful graphic that can visually make the most sense of the relationships between the variables as chapters to readers of the book.

Target Market(s)

Search and Rescue Trackers

Requirements
Must have
• Information listed in project description, and drafted in attached diagrams
Nice to have
• Can include outlines of barefoot and outsoles. While Chapters 1 (Intro), 2 (Missing Persons' Footwear), 10 (Case Studies) and 11 (Summary) are set, the others aren't. The end game of this book is to use the rest of the variables to arrive at the end game, which is measurements for barefoot track length or outsole track length...so those two variables can be highlighted in some way to emphasize their importance.

```html
<!DOCTYPE html>
<html lang="en">
<head>
<meta charset="utf-8">
<title>Sole Relationship Chapter Map</title>
<link href="https://fonts.googleapis.com/css2?family=Roboto+Condensed:wght@400;700&display=swap" rel="stylesheet">
<style>
  :root {
    --green: #228a6f;
    --dark: #4b504d;
    --ink: #3f4441;
    --paper: #ffffff;
    --frame-line: #228a6f;
    --shoe-tone: #e4e4e4;
    --foot-tone: #f2d6d8;
  }
  html, body {
    margin: 0;
    padding: 0;
    width: 1200px;
    height: 675px;
    overflow: hidden;
    background: var(--paper);
  }
  .chart {
    display: block;
    width: 1200px;
    height: 675px;
    font-family: "Roboto Condensed", "Arial Narrow", sans-serif;
  }
  .node-frame { fill: var(--paper); stroke: var(--frame-line); stroke-width: 3; }
  .node-band { fill: var(--green); }
  .node-label { fill: #fff; font-weight: 700; font-size: 19px; text-anchor: middle; }
  .variation-box { fill: var(--dark); }
  .variation-label { fill: #fff; font-weight: 700; font-size: 21px; text-anchor: middle; }
  .shoe-art { fill: var(--shoe-tone); }
  .foot-art { fill: var(--foot-tone); }
  .track-disc { fill: var(--dark); }
  .track-label { fill: var(--ink); font-weight: 700; font-size: 27px; text-anchor: middle; }
  .input-label { fill: var(--ink); font-weight: 700; font-size: 18px; text-anchor: middle; }
  .link-relation { stroke: var(--dark); stroke-width: 4; fill: none; }
  .link-influence { stroke: var(--green); stroke-width: 4; fill: none; }
  .chapter-ring { fill: #fff; stroke: var(--green); stroke-width: 2.2; }
  .chapter-num { fill: var(--green); font-weight: 700; font-size: 16px; text-anchor: middle; dominant-baseline: central; }
  .legend-title { fill: var(--ink); font-weight: 700; font-size: 19px; }
  .legend-frame { fill: none; stroke: var(--dark); stroke-width: 2; }
  .legend-text { fill: var(--ink); font-weight: 700; font-size: 15px; }
</style>
</head>
<body>
<svg class="chart" viewBox="0 0 1280 720" xmlns="http://www.w3.org/2000/svg">
  <defs>
    <marker id="head-relation" viewBox="0 0 10 10" refX="8" refY="5" markerWidth="4" markerHeight="4" orient="auto-start-reverse">
      <path d="M0 0 L10 5 L0 10 z" fill="#4b504d"/>
    </marker>
    <marker id="head-influence" viewBox="0 0 10 10" refX="8" refY="5" markerWidth="4" markerHeight="4" orient="auto-start-reverse">
      <path d="M0 0 L10 5 L0 10 z" fill="#228a6f"/>
    </marker>
  </defs>

  <!-- links -->
  <g class="links">
    <line class="link-influence" x1="170" y1="145" x2="286" y2="145" marker-end="url(#head-influence)"/>
    <line class="link-relation" x1="451" y1="177" x2="792" y2="177" marker-start="url(#head-relation)" marker-end="url(#head-relation)"/>
    <line class="link-relation" x1="953" y1="145" x2="1066" y2="145" marker-end="url(#head-relation)"/>
    <polyline class="link-influence" points="550,288 420,288 420,242" marker-end="url(#head-influence)"/>
    <polyline class="link-influence" points="694,285 874,283 874,242" marker-end="url(#head-influence)"/>
    <line class="link-influence" x1="621" y1="324" x2="621" y2="394" marker-end="url(#head-influence)"/>
    <polyline class="link-relation" points="535,417 375,417 375,242" marker-end="url(#head-relation)"/>
    <line class="link-relation" x1="621" y1="436" x2="621" y2="498" marker-end="url(#head-relation)"/>
    <polyline class="link-relation" points="327,244 327,546 542,546" marker-start="url(#head-relation)" marker-end="url(#head-relation)"/>
    <line class="link-relation" x1="458" y1="596" x2="542" y2="596" marker-end="url(#head-relation)"/>
    <line class="link-relation" x1="697" y1="561" x2="860" y2="561" marker-end="url(#head-relation)"/>
  </g>

  <!-- variable nodes -->
  <g class="node node-insole">
    <rect class="node-frame" x="291" y="89" width="156" height="149"/>
    <rect class="shoe-art" x="302" y="100" width="134" height="96" role="img" aria-label="Shoe outline with insole highlighted in red"/>
    <rect class="node-band" x="291" y="205" width="156" height="34"/>
    <text class="node-label" x="369" y="228">Insole</text>
  </g>
  <g class="node node-outsole">
    <rect class="node-frame" x="797" y="89" width="156" height="149"/>
    <rect class="shoe-art" x="808" y="100" width="134" height="96" role="img" aria-label="Shoe outline with outsole highlighted in red"/>
    <rect class="node-band" x="797" y="205" width="156" height="34"/>
    <text class="node-label" x="875" y="228">Outsole</text>
  </g>
  <g class="node node-barefoot">
    <rect class="node-frame" x="547" y="503" width="150" height="125"/>
    <rect class="foot-art" x="558" y="512" width="128" height="76" role="img" aria-label="Red bare foot in side view"/>
    <rect class="node-band" x="547" y="594" width="150" height="34"/>
    <text class="node-label" x="622" y="617">Barefoot</text>
  </g>
  <g class="node node-size">
    <rect class="node-band" x="535" y="398" width="173" height="38"/>
    <text class="node-label" x="621" y="424">Nominal Size</text>
  </g>
  <g class="node node-variation">
    <rect class="variation-box" x="549" y="245" width="145" height="79" rx="12"/>
    <text class="variation-label" x="621" y="279">Individual</text>
    <text class="variation-label" x="621" y="302">Variation</text>
  </g>

  <!-- inputs -->
  <text class="input-label" x="136" y="139">Hook</text>
  <text class="input-label" x="136" y="160">Area</text>
  <text class="input-label" x="423" y="602">Height</text>

  <!-- track outcomes -->
  <g class="track track-shod">
    <circle class="track-disc" cx="1128" cy="140" r="58" role="img" aria-label="Pair of shoe prints"/>
    <text class="track-label" x="1128" y="234">Shod Track</text>
  </g>
  <g class="track track-barefoot">
    <circle class="track-disc" cx="921" cy="558" r="58" role="img" aria-label="Pair of bare footprints"/>
    <text class="track-label" x="921" y="647">Barefoot Track</text>
  </g>

  <!-- chapter markers -->
  <g class="chapters">
    <circle class="chapter-ring" cx="222" cy="117" r="12"/><text class="chapter-num" x="222" y="118">3</text>
    <circle class="chapter-ring" cx="621" cy="149" r="12"/><text class="chapter-num" x="621" y="150">8</text>
    <circle class="chapter-ring" cx="1008" cy="117" r="12"/><text class="chapter-num" x="1008" y="118">9</text>
    <circle class="chapter-ring" cx="508" cy="313" r="12"/><text class="chapter-num" x="508" y="314">10</text>
    <circle class="chapter-ring" cx="734" cy="313" r="12"/><text class="chapter-num" x="734" y="314">10</text>
    <circle class="chapter-ring" cx="649" cy="353" r="12"/><text class="chapter-num" x="649" y="354">10</text>
    <circle class="chapter-ring" cx="300" cy="389" r="12"/><text class="chapter-num" x="300" y="390">5</text>
    <circle class="chapter-ring" cx="451" cy="457" r="12"/><text class="chapter-num" x="451" y="458">4</text>
    <circle class="chapter-ring" cx="649" cy="466" r="12"/><text class="chapter-num" x="649" y="467">4</text>
    <circle class="chapter-ring" cx="778" cy="533" r="12"/><text class="chapter-num" x="778" y="534">7</text>
    <circle class="chapter-ring" cx="498" cy="621" r="12"/><text class="chapter-num" x="498" y="622">5</text>
  </g>

  <!-- legend -->
  <g class="legend">
    <text class="legend-title" x="68" y="542">LEGEND</text>
    <rect class="legend-frame" x="66" y="557" width="223" height="88"/>
    <circle class="chapter-ring" cx="143" cy="577" r="10"/><text class="chapter-num" x="143" y="578" style="font-size:13px">1</text>
    <text class="legend-text" x="170" y="583">Chapter #</text>
    <line class="link-relation" x1="74" y1="604" x2="150" y2="604" style="stroke-width:3" marker-end="url(#head-relation)"/>
    <text class="legend-text" x="170" y="609">Relationship to</text>
    <line class="link-influence" x1="74" y1="629" x2="150" y2="629" style="stroke-width:3" marker-end="url(#head-influence)"/>
    <text class="legend-text" x="170" y="634">Influence on</text>
  </g>
</svg>
</body>
</html>
```